Business cards Dör Kornhüüs GmbH & Co.KG

We need a uniform business card design template for our employees.
A template should be created to have the same design for all business cards.

Contact Information for Business Card

Firma und Firmierung, Name, Funktion in Unternehmen, Anschrift, Tel. Handynummer, Emailadresse, Internetseite

Colors

Designer to choose colors to be used in the design.

Requirements
Must have
• Our company logo must be on it

```html
<!DOCTYPE html>
<html lang="de">
<head>
<meta charset="utf-8">
<title>Dör Kornhüüs – Visitenkarte</title>
<link rel="stylesheet" href="https://fonts.googleapis.com/css2?family=Open+Sans:wght@400;600;700&display=swap">
<style>
  :root {
    --backdrop: #45423d;
    --card: #292929;
    --lilac: #c9a3d8;
    --pink: #f27a8c;
    --white: #f4f4f4;
    --grey: #b9b9b9;
  }
  * { margin: 0; padding: 0; box-sizing: border-box; }
  html, body { width: 1200px; height: 1200px; overflow: hidden; }
  body {
    background: var(--backdrop);
    font-family: "Open Sans", Arial, sans-serif;
    position: relative;
  }
  .card {
    position: absolute;
    left: 150px;
    width: 900px;
    height: 514px;
    background: var(--card);
    border-radius: 34px;
    box-shadow: 0 14px 36px rgba(0,0,0,.45);
    overflow: hidden;
  }
  .card--front { top: 56px; }
  .card--back { top: 626px; }

  .brand {
    display: flex;
    align-items: center;
    gap: 16px;
    color: var(--lilac);
    font-weight: 600;
    letter-spacing: .5px;
    white-space: nowrap;
  }
  .brand__dot {
    width: 30px; height: 30px;
    border-radius: 50%;
    background: var(--pink);
    flex: none;
  }

  /* front */
  .card--front .brand {
    position: absolute;
    left: 0; right: 0; top: 150px;
    justify-content: center;
    font-size: 68px;
  }
  .web-band {
    position: absolute;
    left: 0; right: 0; top: 330px;
    height: 40px;
  }
  .web-band svg { position: absolute; inset: 0; }
  .web-band__text {
    position: absolute;
    left: 0; right: 0; top: 2px;
    text-align: center;
    color: var(--white);
    font-size: 27px;
    font-weight: 400;
    letter-spacing: .5px;
  }

  /* back */
  .card--back .brand {
    position: absolute;
    left: 100px; top: 62px;
    font-size: 54px;
  }
  .person {
    position: absolute;
    right: 92px; top: 160px;
    text-align: right;
  }
  .person__name {
    color: var(--lilac);
    font-size: 34px;
    font-weight: 700;
    letter-spacing: .5px;
    line-height: 1.1;
  }
  .person__role {
    color: var(--grey);
    font-size: 19px;
    line-height: 1.3;
  }
  .divider {
    position: absolute;
    left: 200px; right: 88px; top: 248px;
    height: 3px;
    background: var(--lilac);
  }
  .contacts {
    position: absolute;
    left: 210px; top: 264px;
    list-style: none;
  }
  .contacts li {
    display: flex;
    align-items: center;
    gap: 14px;
    color: var(--white);
    font-size: 20px;
    line-height: 34px;
    white-space: nowrap;
  }
  .contacts .contacts__company {
    color: var(--lilac);
    font-weight: 600;
  }
  .contacts svg { width: 20px; height: 20px; flex: none; }
</style>
</head>
<body>

<section class="card card--front" aria-label="Visitenkarte Vorderseite">
  <div class="brand"><span class="brand__dot"></span>Dör Kornhüüs</div>
  <div class="web-band">
    <svg viewBox="0 0 900 40" preserveAspectRatio="none" aria-hidden="true">
      <polygon points="40,40 250,0 250,18" fill="var(--pink)"/>
      <polygon points="650,22 650,40 860,0" fill="var(--pink)"/>
    </svg>
    <div class="web-band__text">WWW.WEBSITEHERE.COM</div>
  </div>
</section>

<section class="card card--back" aria-label="Visitenkarte Rückseite">
  <div class="brand"><span class="brand__dot"></span>Dör Kornhüüs</div>

  <div class="person">
    <div class="person__name">LENE JANSEN</div>
    <div class="person__role">Manager</div>
  </div>

  <div class="divider"></div>

  <ul class="contacts">
    <li class="contacts__company">
      <svg viewBox="0 0 20 20" aria-hidden="true"><rect x="3" y="3" width="14" height="14" fill="none" stroke="var(--pink)" stroke-width="1.8"/><path d="M7 7h2M11 7h2M7 11h2M11 11h2" stroke="var(--pink)" stroke-width="1.8"/></svg>
      Dör Kornhüüs GmbH &amp; Co.KG
    </li>
    <li>
      <svg viewBox="0 0 20 20" aria-hidden="true"><path d="M10 1.5a6 6 0 0 0-6 6c0 4.5 6 11 6 11s6-6.5 6-11a6 6 0 0 0-6-6z" fill="var(--pink)"/><circle cx="10" cy="7.5" r="2.2" fill="var(--card)"/></svg>
      Mühlenweg 12, 00000 Musterstadt
    </li>
    <li>
      <svg viewBox="0 0 20 20" aria-hidden="true"><rect x="5" y="1.5" width="10" height="17" rx="2" fill="none" stroke="var(--pink)" stroke-width="1.8"/><circle cx="10" cy="15.5" r="1.1" fill="var(--pink)"/></svg>
      +0000 -000- 0000
    </li>
    <li>
      <svg viewBox="0 0 20 20" aria-hidden="true"><path d="M5 2.5l3 3.5-1.8 2a10 10 0 0 0 5.8 5.8l2-1.8 3.5 3-2 2.5C8.5 17.5 2.5 11.5 2.5 4.5z" fill="var(--pink)"/></svg>
      +0000 -000- 0000
    </li>
    <li>
      <svg viewBox="0 0 20 20" aria-hidden="true"><rect x="1.5" y="4" width="17" height="12" fill="var(--pink)"/><path d="M1.5 4l8.5 7 8.5-7" fill="none" stroke="var(--card)" stroke-width="1.5"/></svg>
      email@addresshere.com
    </li>
    <li>
      <svg viewBox="0 0 20 20" aria-hidden="true"><g fill="none" stroke="var(--pink)" stroke-width="1.5"><circle cx="10" cy="10" r="8"/><ellipse cx="10" cy="10" rx="3.5" ry="8"/><path d="M2 10h16M3.5 6h13M3.5 14h13"/></g></svg>
      www.websitehere.com
    </li>
  </ul>
</section>

</body>
</html>
```